website refresh with jungle and/or gorilla theme for marketing agency

Our marketing agency needs a creative website boost. The website (which is Wordpress) is:https://www.tallmoosestudio.com. Given our name, we would like to have a jungle/gorilla theme. The Moose website should have a beastly presence. See the site now and how the gorilla is in your face. The text can remain the same, we just need a new layout and/or graphics. What other direction can I give? Not sure, we will know it when we see it.

Target Market(s)

small and medium sized businesses

Industry/Entity Type

Digital Marketing

Number of Pages Required

1 page

Colors

Designer to choose colors to be used in the design.

Requirements
Must have
• I don't really have any must have's. I don't want to limit the creativity of the designer.
Nice to have
• I am encouraging an out of the box design, something that isn't so "boxy" and traditional like the other sites.
Should not have
• I don't like standard looking sites that have a boxy layout with your standard cartoon and/or basic icons.

```html
<!DOCTYPE html>
<html lang="en">
<head>
<meta charset="utf-8">
<title>Moose Marketing</title>
<link rel="stylesheet" href="https://fonts.googleapis.com/css2?family=Montserrat:wght@400;500;600;700&family=Open+Sans:wght@400;600;700&family=Exo+2:wght@600;700&display=swap">
<style>
:root{
  --ink:#1f1f1f;
  --body:#555;
  --blue:#56a8d8;
  --accent:#4aa6e0;
  --white:#fff;
  --grey:#ececec;
  --dark:#2c2c2c;
  --line:#222;
}
*{box-sizing:border-box;margin:0;padding:0}
html,body{width:1200px;height:3829px;overflow:hidden}
body{position:relative;background:var(--white);font-family:"Open Sans",Arial,sans-serif;color:var(--ink)}
.abs{position:absolute}
h2.section-title{position:absolute;left:0;width:1200px;text-align:center;font-family:"Montserrat",sans-serif;font-weight:500;font-size:38px;color:var(--ink)}
.title-bar{position:absolute;left:570px;width:60px;height:6px;background:var(--line)}

/* hero */
.hero{position:absolute;left:0;top:0;width:1200px;height:720px;overflow:hidden;
  background:radial-gradient(ellipse at 30% 40%,#4a4a47 0%,#2a2a28 45%,#161615 100%)}
.hero-photo{position:absolute;inset:0}
.brand{position:absolute;left:221px;top:44px;width:103px;height:77px;background:#3f93c8;display:flex;align-items:center;justify-content:center;
  font-family:"Montserrat",sans-serif;font-weight:700;font-size:22px;color:var(--white);text-transform:uppercase}
.main-nav{position:absolute;top:70px;left:504px;display:flex;gap:0}
.main-nav a{position:absolute;white-space:nowrap;color:var(--white);text-decoration:none;font-family:"Montserrat",sans-serif;font-size:16px;font-weight:500}
.hero-title{position:absolute;left:655px;top:262px;font-family:"Exo 2",sans-serif;font-weight:700;font-size:40px;line-height:52px;color:var(--white)}
.hero-title .hl{color:var(--accent)}
.hero-rule{position:absolute;left:790px;top:392px;width:187px;height:5px;background:var(--white)}
.hero-sub{position:absolute;left:655px;top:428px;width:330px;font-size:17px;line-height:26px;color:var(--white)}
.start-btn{position:absolute;left:701px;top:512px;width:88px;height:53px;border:2px solid var(--accent);border-left:none;
  color:var(--accent);font-family:"Montserrat",sans-serif;font-size:15px;font-weight:600;display:flex;align-items:center}
.start-btn span{margin-left:0}

/* about */
.about-title{position:absolute;left:221px;top:788px;font-family:"Montserrat",sans-serif;font-weight:500;font-size:40px}
.about-bar{position:absolute;left:221px;top:842px;width:110px;height:5px;background:var(--line)}
.about-text{position:absolute;left:221px;top:856px;width:740px;font-size:11px;line-height:15px;color:var(--body)}
.feature{position:absolute;top:943px;width:200px;text-align:center}
.feature .icon{width:70px;height:70px;border-radius:50%;background:#ececec;margin:0 auto;display:flex;align-items:center;justify-content:center}
.feature p{margin-top:16px;font-family:"Montserrat",sans-serif;font-size:16px;color:#333}

/* why */
.why{position:absolute;left:0;top:1118px;width:1200px;height:475px;background:var(--blue)}
.why h2{position:absolute;top:72px;left:0;width:1200px;text-align:center;font-family:"Montserrat",sans-serif;font-weight:500;font-size:38px;color:var(--white)}
.why .bar{position:absolute;left:570px;top:124px;width:60px;height:6px;background:var(--white)}
.why-text{position:absolute;left:270px;top:142px;width:660px;text-align:center;font-size:10.5px;line-height:15px;color:var(--white)}
.why-text p+p{margin-top:12px}
.video{position:absolute;left:278px;top:1360px;width:644px;height:264px;
  background:linear-gradient(90deg,#c76a1c 0%,#8a5a2c 30%,#d9d4cc 55%,#e9e6e1 100%)}
.play{position:absolute;left:581px;top:1472px}
.slide-arrow{position:absolute}

/* testimonial */
.portrait{position:absolute;border-radius:50%;border:3px solid var(--accent)}
.quote{position:absolute;left:360px;top:1980px;width:480px;text-align:center;font-size:15px;line-height:25px;color:#444}
.cite{position:absolute;left:0;top:2092px;width:1200px;text-align:center;font-weight:700;font-size:14px;color:#222}

/* cause */
.cause-panel{position:absolute;left:0;top:2226px;width:619px;height:429px;background:var(--grey)}
.cause-photo{position:absolute;left:619px;top:2192px;width:581px;height:463px;
  background:linear-gradient(180deg,#7d7a72 0%,#a9a79f 35%,#e8ecf0 65%,#f4f6f8 100%)}
.cause-head{position:absolute;left:221px;top:2266px;width:360px;font-family:"Montserrat",sans-serif;font-weight:500;font-size:36px;line-height:48px;color:var(--ink)}
.cause-rule{position:absolute;left:221px;top:2420px;width:85px;height:5px;background:var(--line)}
.cause-num{position:absolute;left:221px;top:2450px;font-family:"Montserrat",sans-serif;font-weight:500;font-size:70px;color:var(--ink)}
.cause-note{position:absolute;left:221px;top:2560px;width:380px;font-size:15px;line-height:26px;color:#888}
.cause-note b{color:var(--ink);font-weight:600}

/* brands */
.brand-box{position:absolute;left:85px;top:2814px;width:1015px;height:226px;background:var(--grey)}
.brand-row{position:absolute;left:85px;top:2814px;width:1015px;height:147px;background:var(--white);display:flex;justify-content:center;align-items:center;gap:90px}
.client{display:flex;align-items:center;gap:10px;font-family:"Open Sans",sans-serif;font-weight:600;font-size:24px;color:#333}
.client i{display:block;width:18px;height:18px;background:#6dbd45}
.client.c2 i{background:#c21d2f;border-radius:50%}
.client.c3 i{background:#f2a319}

/* contact */
.contact{position:absolute;left:0;top:3110px;width:1200px;height:629px;background:var(--dark)}
.contact h2{position:absolute;top:72px;left:0;width:1200px;text-align:center;font-family:"Montserrat",sans-serif;font-weight:500;font-size:36px;color:var(--white)}
.contact .bar{position:absolute;left:570px;top:122px;width:60px;height:6px;background:var(--white)}
.field{position:absolute;background:var(--white);font-size:9px;color:#888;padding:12px 10px;text-transform:uppercase;letter-spacing:.3px}
.captcha{position:absolute;left:221px;top:3552px;width:170px;height:39px;background:#f9f9f9;border:1px solid #d3d3d3;display:flex;align-items:center;gap:8px;padding-left:10px;font-size:9px;color:#333}
.captcha .box{width:14px;height:14px;border:2px solid #c1c1c1;background:var(--white)}
.captcha .mark{margin-left:auto;margin-right:10px;width:18px;height:18px;border-radius:50%;background:#7a9fd6}
.submit{position:absolute;left:221px;top:3618px;width:84px;height:42px;border:2px solid var(--accent);border-left:none;color:var(--accent);font-family:"Montserrat",sans-serif;font-size:14px;font-weight:600;display:flex;align-items:center}
.contact-info{position:absolute;left:743px;top:3278px;color:var(--white)}
.contact-info h3{font-family:"Montserrat",sans-serif;font-weight:600;font-size:20px}
.info-line{display:flex;gap:14px;font-size:15px;line-height:21px;margin-top:12px}
.follow{margin-top:36px}
.socials{display:flex;gap:14px;margin-top:14px}
.socials span{display:block;width:30px;height:30px;border:2px solid var(--white)}

/* footer */
.footer-links{position:absolute;left:0;top:3762px;width:1200px;text-align:center;font-size:10px;font-weight:600;color:#222;letter-spacing:.3px}
.footer-links span{margin:0 8px;color:#888}
.copyright{position:absolute;left:0;top:3790px;width:1200px;text-align:center;font-size:9px;font-weight:600;color:#222}
</style>
</head>
<body>

<header class="hero">
  <div class="hero-photo" role="img" aria-label="Close-up photograph of a gorilla's face in dark tones filling the hero"></div>
  <div class="brand">Moose</div>
  <nav class="main-nav">
    <a style="left:0">HOME</a>
    <a style="left:92px">ABOUT</a>
    <a style="left:185px">LEARN</a>
    <a style="left:275px">PORTFOLIO</a>
    <a style="left:403px">CONTACT</a>
  </nav>
  <h1 class="hero-title">Social and<br><span class="hl">Search Marketing</span><br>Beasts</h1>
  <div class="hero-rule"></div>
  <p class="hero-sub">Get performance driven digital marketing leaders on your team</p>
  <div class="start-btn"><span>Start &nbsp;&#8594;</span></div>
</header>

<section>
  <h2 class="about-title">About</h2>
  <div class="about-bar"></div>
  <p class="about-text">What sets us apart from other marketing agencies is our team of A-players. Each team member has proven themselves to be in the top 1% of all marketers. They are the 1 percenters who are passionate about what they do and have proven experience to back up their incredible skill sets. Led by our founder, who has built and sold 4 companies himself and written 4 books, the team at Moose Marketing specializes in user acquisition, lead generation, and brand stability.</p>
  <div class="feature" style="left:237px">
    <div class="icon"><svg width="36" height="36" viewBox="0 0 36 36" fill="none" stroke="#333" stroke-width="1.6"><rect x="5" y="6" width="26" height="18"/><path d="M18 24v6M12 32l6-2 6 2M9 20l6-6 4 4 8-8"/></svg></div>
    <p>Get More Traffic</p>
  </div>
  <div class="feature" style="left:499px">
    <div class="icon"><svg width="38" height="36" viewBox="0 0 38 36" fill="none" stroke="#333" stroke-width="1.6"><circle cx="13" cy="12" r="4"/><circle cx="25" cy="12" r="4"/><path d="M5 26c0-5 4-8 8-8s8 3 8 8M17 26c0-5 4-8 8-8s8 3 8 8"/></svg></div>
    <p>Higher Quality Leads</p>
  </div>
  <div class="feature" style="left:761px">
    <div class="icon"><svg width="36" height="36" viewBox="0 0 36 36" fill="none" stroke="#333" stroke-width="1.6"><path d="M5 31h26M8 31v-6h4v6M15 31v-10h4v10M22 31v-14h4v14M7 19l8-7 5 3 10-9M26 6h4v4"/></svg></div>
    <p>Get More sales</p>
  </div>
</section>

<section class="why">
  <h2>Why Moose Marketing?</h2>
  <div class="bar"></div>
  <div class="why-text">
    <p>Moose Marketing is the apex predator of the social and search marketing industries. We are senior marketing experts with the skills to create revenue-producing marketing funnels. In this age of big data, there is no better way to reach instant visibility with your audience than to have a fit team of skilled pros on your side.</p>
    <p>Is your marketing funnel maximizing revenue and conversions? Learn the single biggest mistake companies make in their marketing funnel and how to fix it.</p>
  </div>
</section>
<svg class="slide-arrow" style="left:218px;top:1478px" width="16" height="26" viewBox="0 0 16 26"><path d="M13 2L3 13l10 11" stroke="#fff" stroke-width="3" fill="none"/></svg>
<svg class="slide-arrow" style="left:963px;top:1478px" width="16" height="26" viewBox="0 0 16 26"><path d="M3 2l10 11L3 24" stroke="#fff" stroke-width="3" fill="none"/></svg>
<div class="video" role="img" aria-label="Video still of a person writing notes at a desk beside a laptop"></div>
<svg class="play" width="38" height="38" viewBox="0 0 38 38"><circle cx="19" cy="19" r="16" fill="none" stroke="#fff" stroke-width="3"/><path d="M15 12l11 7-11 7z" fill="#fff"/></svg>

<section>
  <h2 class="section-title" style="top:1695px">Why Moose Marketing?</h2>
  <div class="title-bar" style="top:1748px"></div>
  <svg class="slide-arrow" style="left:218px;top:1874px" width="30" height="30" viewBox="0 0 30 30"><circle cx="15" cy="15" r="14" fill="#e2e2e2"/><path d="M17 9l-6 6 6 6" stroke="#fff" stroke-width="2.5" fill="none"/></svg>
  <svg class="slide-arrow" style="left:951px;top:1874px" width="30" height="30" viewBox="0 0 30 30"><circle cx="15" cy="15" r="14" fill="#e2e2e2"/><path d="M13 9l6 6-6 6" stroke="#fff" stroke-width="2.5" fill="none"/></svg>
  <div class="portrait" role="img" aria-label="Portrait of a client in a suit" style="left:410px;top:1815px;width:150px;height:150px;background:linear-gradient(160deg,#8a7a6e,#3a3f4a)"></div>
  <div class="portrait" role="img" aria-label="Portrait of a client in a suit" style="left:640px;top:1815px;width:150px;height:150px;background:linear-gradient(160deg,#cfc7bd,#8a7d72)"></div>
  <div class="portrait" role="img" aria-label="Portrait of the quoted client, a founder in a suit" style="left:505px;top:1788px;width:190px;height:190px;background:linear-gradient(160deg,#dcdad6,#4a5260)"></div>
  <p class="quote">"For the same price of hiring one person in-house, I am a getting a team of senior marketers that constantly innovate and explore revenue opportunities. I highly recommend the team at Moose Marketing."</p>
  <p class="cite">Daria Holt, Founder, Brightpath Goods</p>
</section>

<section>
  <div class="cause-panel"></div>
  <div class="cause-photo" role="img" aria-label="Photograph of a team of sled dogs running through snow"></div>
  <p class="cause-head">In 2017, we helped 362 dogs. In 2018 we helped...</p>
  <div class="cause-rule"></div>
  <p class="cause-num">220</p>
  <p class="cause-note">abused and/or homeless dogs through the <b>Paws Haven</b> <b>dog foundation.</b></p>
</section>

<section>
  <h2 class="section-title" style="top:2725px">Name Brands We've Worked For</h2>
  <div class="title-bar" style="top:2776px"></div>
  <div class="brand-box"></div>
  <div class="brand-row">
    <div class="client"><i></i>Northwire</div>
    <div class="client c2"><i></i>Calloway Apparel</div>
    <div class="client c3"><i></i>Summit Trust</div>
  </div>
</section>

<section class="contact">
  <h2>Contact Moose Marketing</h2>
  <div class="bar"></div>
</section>
<div class="field" style="left:221px;top:3264px;width:504px;height:44px">Name</div>
<div class="field" style="left:221px;top:3323px;width:244px;height:44px">Email Address</div>
<div class="field" style="left:479px;top:3323px;width:246px;height:44px">Phone Number</div>
<div class="field" style="left:221px;top:3380px;width:504px;height:141px">How can we help?</div>
<div class="captcha"><span class="box"></span>I'm not a robot<span class="mark"></span></div>
<div class="submit">Submit &nbsp;&#8594;</div>
<div class="contact-info">
  <h3>Adress</h3>
  <div class="info-line"><svg width="10" height="16" viewBox="0 0 10 16"><rect x="1" y="1" width="8" height="14" rx="1.5" fill="none" stroke="#4aa6e0" stroke-width="1.6"/></svg>555-014-2290,</div>
  <div class="info-line"><svg width="12" height="16" viewBox="0 0 12 16"><path d="M6 15s5-5.5 5-9A5 5 0 0 0 1 6c0 3.5 5 9 5 9z" fill="#4aa6e0"/><circle cx="6" cy="6" r="1.8" fill="#2c2c2c"/></svg><span>48 Fernbrook Ln, Alder<br>Springs CA 95012</span></div>
  <h3 class="follow">Follow Us</h3>
  <div class="socials"><span></span><span></span></div>
</div>

<footer>
  <p class="footer-links">HOME<span>|</span>ABOUT<span>|</span>LEARN<span>|</span>PORTFOLIO<span>|</span>CONTACT<span>|</span>PRIVACY<span>|</span>POLICY<span>|</span>TERMS AND CONDITIONS</p>
  <p class="copyright">COPYRIGHT MOOSE Marketing ALL RIGHTS RESERVED</p>
</footer>

</body>
</html>
```